Verdanix Medical Business Card

Create a high class Business card for Medical Aesthetics and Wellness Practice called Verdanix Medical Aesthetics and Wellness as per the logo attached.
Addresss is: 418 Harlan Brook Road Suite 312 Melville, New York 11093
Phone (555)204-7391 IG @verdanix_medical
Verdanixmedical.example

I need 5 different name configurations
1) Dr. Theo Valcourt
Aesthetics and Wellness Specialist
Medical Director

2) Rosalind Pettinger, NP
Clinical Nurse Manager

3) Marla Vostrik, RN
Aesthetic Nurse Specialist

4) Petra Halvesen, RN

5) Dana Kowbeck, L.E.
Senior Licensed Esthetician

Target Market(s)

22-55 Females

Industry/Entity Type

Medical Spa and Wellness

Contact Information for Business Card

Logo, address, phone, web, instagram, providers name

Requirements
Must have
• Attractive classy modern look

```html
<!DOCTYPE html>
<html lang="en">
<head>
<meta charset="utf-8">
<title>Verdanix Medical Business Card</title>
<link href="https://fonts.googleapis.com/css2?family=Montserrat:wght@400;500;700&display=swap" rel="stylesheet">
<style>
  :root {
    --backdrop: #8f8d8e;
    --card: #ffffff;
    --deep-teal: #134f5f;
    --aqua: #67c3c6;
    --ink-light: #ffffff;
  }
  * { margin: 0; padding: 0; box-sizing: border-box; }
  html, body {
    width: 1200px; height: 1200px; overflow: hidden;
    background: var(--backdrop);
    font-family: "Montserrat", Arial, sans-serif;
  }
  .canvas { position: relative; width: 1200px; height: 1200px; }
  .card {
    position: absolute; left: 151px; width: 897px; height: 525px;
    background: var(--card);
    box-shadow: 4px 6px 14px rgba(0,0,0,0.35);
    overflow: hidden;
  }
  .card--front { top: 46px; }
  .card--back { top: 619px; }

  .accent-strip {
    position: absolute; left: 768px; top: 38px; width: 79px; height: 450px;
    background: var(--aqua);
  }
  .info-panel {
    position: absolute; left: 0; top: 38px; width: 822px; height: 450px;
    background: var(--deep-teal);
    border-radius: 0 50px 50px 0;
    color: var(--ink-light);
  }
  .provider-name {
    position: absolute; left: 77px; top: 64px;
    font-size: 37px; font-weight: 700; letter-spacing: 0.2px;
  }
  .provider-role {
    position: absolute; left: 77px;
    font-size: 22px; font-weight: 400;
  }
  .provider-role--specialty { top: 109px; }
  .provider-role--title { top: 146px; }

  .contact-list { position: absolute; left: 77px; top: 220px; list-style: none; }
  .contact-item {
    display: flex; align-items: flex-start;
    font-size: 22px; line-height: 37.5px; font-weight: 400;
  }
  .contact-icon { width: 18px; height: 18px; margin-top: 10px; margin-right: 23px; flex: none; }
  .contact-text { line-height: 30px; padding-top: 4px; }

  .brand-block {
    position: absolute; left: 0; right: 0; top: 150px;
    text-align: center; color: var(--deep-teal);
  }
  .brand-name {
    font-size: 100px; font-weight: 400; letter-spacing: 8px; line-height: 1;
  }
  .brand-tagline {
    margin-top: 32px; font-size: 25px; font-weight: 500; letter-spacing: 1.5px;
  }
  .brand-location {
    margin-top: 20px; font-size: 17px; font-weight: 400; letter-spacing: 9px;
  }
</style>
</head>
<body>
<main class="canvas">
  <section class="card card--front">
    <div class="accent-strip"></div>
    <div class="info-panel">
      <h1 class="provider-name">Dr. Theo Valcourt</h1>
      <p class="provider-role provider-role--specialty">Aesthetics and Wellness Specialist</p>
      <p class="provider-role provider-role--title">Medical Director</p>
      <ul class="contact-list">
        <li class="contact-item">
          <svg class="contact-icon" viewBox="0 0 24 24" aria-hidden="true"><path fill="#fff" d="M6.6 10.8c1.4 2.8 3.8 5.1 6.6 6.6l2.2-2.2c.3-.3.7-.4 1-.2 1.1.4 2.3.6 3.6.6.6 0 1 .4 1 1V20c0 .6-.4 1-1 1C10.6 21 3 13.4 3 4c0-.6.4-1 1-1h3.5c.6 0 1 .4 1 1 0 1.3.2 2.5.6 3.6.1.3 0 .7-.2 1z"/></svg>
          <span class="contact-text">(555) 204-7391</span>
        </li>
        <li class="contact-item">
          <svg class="contact-icon" viewBox="0 0 24 24" aria-hidden="true"><rect x="3" y="3" width="18" height="18" rx="4" fill="none" stroke="#fff" stroke-width="2.4"/></svg>
          <span class="contact-text">@verdanix_medical</span>
        </li>
        <li class="contact-item">
          <svg class="contact-icon" viewBox="0 0 24 24" aria-hidden="true"><g fill="none" stroke="#fff" stroke-width="1.8"><circle cx="12" cy="12" r="9.5"/><ellipse cx="12" cy="12" rx="4" ry="9.5"/><path d="M2.5 12h19M4 7h16M4 17h16"/></g></svg>
          <span class="contact-text">Verdanixmedical.example</span>
        </li>
        <li class="contact-item">
          <svg class="contact-icon" viewBox="0 0 24 24" aria-hidden="true"><path fill="#fff" d="M12 2a7 7 0 0 0-7 7c0 5.2 7 13 7 13s7-7.8 7-13a7 7 0 0 0-7-7zm0 9.5A2.5 2.5 0 1 1 12 6.5a2.5 2.5 0 0 1 0 5z"/></svg>
          <span class="contact-text">418 Harlan Brook Road<br>Suite 312 Melville, New York 11093</span>
        </li>
      </ul>
    </div>
  </section>

  <section class="card card--back">
    <div class="brand-block">
      <p class="brand-name">verdanix</p>
      <p class="brand-tagline">MEDICAL AESTHETICS AND WELLNESS</p>
      <p class="brand-location">NEW YORK</p>
    </div>
  </section>
</main>
</body>
</html>
```